Create a Graphic About YOURSELF and PixelHarbor

PixelHarbor would like you (designers) to create an awesome graphic to promote YOURSELF and your profile on PixelHarbor!

Your graphic should communicate your name, your services and should mention PixelHarbor.

The design should be perfect for sharing on Chatterly. Here's an example of what we'd like http://blog.pixelharbor-example.ca/article/333/pixelharbor-launches-3000-hire-me-social-design-contest

Once you submitted your design, we'd love you to share the design ('advertisement') and promote yourself and PixelHarbor to your friends and potential customers. So make your submissions great and get your friends to vote for your design by 'Liking' it on Chatterly!

Prizes:
$1500 - "PixelHarbor Community" prize awarded to the designer with the most Chatterly 'Likes'
5 x $50 for the next 5 'most liked' designs on Chatterly

$1000 - "Hire Me" prize awarded to the designer who receives the most client invites
5 x $50 for the next 5 'most invited' designers

In summary, this is a great opportunity for you to increase your exposure to PixelHarbor customers and win cash prizes. Show off your design skills and get hired by PixelHarbor customers from around the world!

Target Market(s)

Fans, friends and customers of YOU

Industry/Entity Type

Cash

Requirements
Must have
• 1) Include your PixelHarbor user name on the graphic so customers can find you in the PixelHarbor Designer Directory
2) Include the tagline "Hire Me on PixelHarbor.com!" in your graphic design.
3) Share your design's URL on our Chatterly wall at http://chatterly-example.com/pixelharbor and get your friends to 'like' your design.
Nice to have
• 1) Include a tagline that expresses your design approach/philosophy
2) Artwork dimensions: 403 x 403 px
3) You can submit more than 1 design!
Should not have
• You must own the copyright of any images you use including stock imagery.

```html
<!DOCTYPE html>
<html lang="en">
<head>
<meta charset="utf-8">
<title>Hire Me on PixelHarbor.com</title>
<link rel="stylesheet" href="https://fonts.googleapis.com/css2?family=Archivo+Black&family=Work+Sans:wght@300;700&display=swap">
<style>
  :root {
    --paper: #ffffff;
    --ink: #111111;
  }
  html, body {
    margin: 0;
    padding: 0;
    width: 1200px;
    height: 1200px;
    overflow: hidden;
    background: var(--paper);
  }
  .poster {
    position: relative;
    width: 1200px;
    height: 1200px;
    background: var(--paper);
    color: var(--ink);
  }
  .headline {
    position: absolute;
    left: 351px;
    width: 513px;
    margin: 0;
  }
  .headline-line {
    position: absolute;
    left: 0;
    width: 100%;
    display: block;
    text-align: justify;
    text-align-last: justify;
    white-space: nowrap;
    line-height: 1;
  }
  .line-light {
    font-family: "Work Sans", sans-serif;
    font-weight: 300;
  }
  .line-bold {
    font-family: "Archivo Black", sans-serif;
    font-weight: 400;
  }
  .line-want   { top: 408px; font-size: 62px; }
  .line-design { top: 458px; font-size: 146px; letter-spacing: -2px; }
  .line-stand  { top: 588px; font-size: 53px; }
  .line-from   { top: 627px; font-size: 66px; }
  .line-crowd  { top: 680px; font-size: 128px; letter-spacing: -3px; }

  .side-tagline {
    position: absolute;
    left: 1176px;
    top: 752px;
    margin: 0;
    transform: translate(-50%, -50%) rotate(-90deg);
    font-family: "Work Sans", sans-serif;
    font-weight: 700;
    font-size: 22px;
    letter-spacing: 0.5px;
    white-space: nowrap;
    text-transform: uppercase;
  }
  .corner-block {
    position: absolute;
    left: 1057px;
    top: 968px;
    width: 143px;
    height: 143px;
    background: var(--ink);
  }
</style>
</head>
<body>
  <main class="poster">
    <h1 class="headline">
      <span class="headline-line line-light line-want">WANT YOUR</span>
      <span class="headline-line line-bold line-design">DESIGN</span>
      <span class="headline-line line-light line-stand">TO STAND OUT</span>
      <span class="headline-line line-light line-from">FROM THE</span>
      <span class="headline-line line-bold line-crowd">CROWD?</span>
    </h1>
    <p class="side-tagline">Hire me on PixelHarbor.com</p>
    <div class="corner-block" aria-hidden="true"></div>
  </main>
</body>
</html>
```